Business Card- Can you make it cool vs boring!

Need a refresh on my business card! Want it to be modern but simple, classic and a pop of coolness! we do senior living and it is boring. but that doesn't mean our business card have to look boring! Open to two sided cards. our website is www.Tolbera-KM.com

Target Market(s)

capital market

Industry/Entity Type

senior housing/ real estate

Contact Information for Business Card

logo/ name/ cell/ address/ www.Tolbera-KM.com/ space for a QR code

Requirements
Must have
• maybe a QR code (do not make prominent I may not use the QR so design where it can be taken out) that link to more about us/ landing page. needs to be modern but clean
Should not have
• clip art or script

```html
<!DOCTYPE html>
<html lang="en">
<head>
<meta charset="utf-8">
<title>Tolbera Senior Living – Business Card</title>
<link href="https://fonts.googleapis.com/css2?family=Montserrat:wght@400;500;700&display=swap" rel="stylesheet">
<style>
  :root {
    --backdrop: #9b9b9b;
    --card-dark: #262626;
    --card-dark-ink: #121212;
    --card-light: #f4f2ed;
    --accent: #dd6f2a;
    --ink: #2a2a2a;
    --muted: #8d8b88;
    --rule: #c9c6c0;
  }
  * { margin: 0; padding: 0; box-sizing: border-box; }
  html, body {
    width: 1200px; height: 1000px; overflow: hidden;
    background: var(--backdrop);
    font-family: "Montserrat", sans-serif;
  }
  .canvas { position: relative; width: 1200px; height: 1000px; }

  .card {
    position: absolute; left: 296px; width: 607px; height: 350px;
    border-radius: 26px; overflow: hidden;
  }
  .card--front { top: 129px; background: var(--card-dark); }
  .card--back  { top: 534px; background: var(--card-light); }

  .wordmark {
    position: absolute; left: 0; right: 0; text-align: center;
    font-family: "Montserrat", sans-serif; font-weight: 500;
  }
  .wordmark__name { display: block; letter-spacing: 1px; }
  .wordmark__tag  { display: block; letter-spacing: 2px; }

  .card--front .wordmark { top: 112px; color: var(--card-dark-ink); }
  .card--front .wordmark__name { font-size: 78px; line-height: 82px; }
  .card--front .wordmark__tag  { font-size: 22px; line-height: 28px; margin-top: 4px; }

  .card--back .wordmark { top: 40px; color: var(--accent); }
  .card--back .wordmark__name { font-size: 44px; line-height: 48px; }
  .card--back .wordmark__tag  { font-size: 12px; line-height: 16px; margin-top: 4px; }

  .person {
    position: absolute; right: 326px; top: 176px; text-align: right;
  }
  .person__name { font-weight: 700; font-size: 21px; color: var(--accent); line-height: 28px; }
  .person__title { font-weight: 500; font-size: 16px; color: var(--ink); line-height: 22px; margin-top: 5px; }

  .divider {
    position: absolute; left: 303px; top: 172px; width: 1px; height: 62px;
    background: var(--rule);
  }

  .contact { position: absolute; left: 326px; top: 174px; list-style: none; }
  .contact__item {
    display: flex; align-items: center; gap: 9px;
    font-size: 16px; color: var(--ink); line-height: 20.5px;
  }
  .contact__icon { width: 12px; height: 12px; fill: var(--accent); flex: none; }

  .address {
    position: absolute; left: 0; right: 0; top: 297px; text-align: center;
    font-size: 13px; line-height: 17px; color: var(--muted);
  }
</style>
</head>
<body>
<main class="canvas">

  <section class="card card--front" aria-label="Card front">
    <div class="wordmark">
      <span class="wordmark__name">Tolbera</span>
      <span class="wordmark__tag">SENIOR LIVING</span>
    </div>
  </section>

  <section class="card card--back" aria-label="Card back">
    <div class="wordmark">
      <span class="wordmark__name">Tolbera</span>
      <span class="wordmark__tag">SENIOR LIVING</span>
    </div>

    <div class="person">
      <p class="person__name">Name Surname</p>
      <p class="person__title">Title</p>
    </div>

    <div class="divider"></div>

    <ul class="contact">
      <li class="contact__item">
        <svg class="contact__icon" viewBox="0 0 24 24" aria-hidden="true"><path d="M6.6 10.8a15.1 15.1 0 0 0 6.6 6.6l2.2-2.2c.3-.3.7-.4 1-.2 1.1.4 2.3.6 3.6.6.6 0 1 .4 1 1V20c0 .6-.4 1-1 1A17 17 0 0 1 3 4c0-.6.4-1 1-1h3.5c.6 0 1 .4 1 1 0 1.3.2 2.5.6 3.6.1.3 0 .7-.2 1z"/></svg>
        (555) 014-2738
      </li>
      <li class="contact__item">
        <svg class="contact__icon" viewBox="0 0 24 24" aria-hidden="true"><path d="M2 5h20v14H2z M3.5 6.5 12 13l8.5-6.5" stroke="#f4f2ed" stroke-width="1.5"/></svg>
        info@tolbera-km.com
      </li>
      <li class="contact__item">
        <svg class="contact__icon" viewBox="0 0 24 24" aria-hidden="true"><circle cx="12" cy="12" r="10"/><path d="M2 12h20M12 2c3 3 3 17 0 20M12 2c-3 3-3 17 0 20M4 7h16M4 17h16" stroke="#f4f2ed" stroke-width="1.2" fill="none"/></svg>
        tolbera-km.com
      </li>
    </ul>

    <address class="address" style="font-style: normal;">
      418 Maple Crest Lane, Suite #210<br>
      Harlow Springs, TX 75012
    </address>
  </section>

</main>
</body>
</html>
```